Briefpapier und Visitenkarten
Zielgruppe
Das Design soll Herren im mittleren bis hohen Alter ansprechen.
Aufgabenstellung
Benötigt wird ein Briefpapier für die Koresspondenz und die Rechnungen. Ein Logo ist vorhanden und muss ins Briefpapier und auf die Visitenkarten einbebunden werden.

```html
<!DOCTYPE html>
<html lang="de">
<head>
<meta charset="utf-8">
<title>Briefpapier Velmora Systemhaus</title>
<link href="https://fonts.googleapis.com/css2?family=Arimo:wght@400;700&display=swap" rel="stylesheet">
<style>
  :root {
    --brand-red: #d0131c;
    --ink: #111111;
    --band-black: #0e0e12;
    --paper: #ffffff;
    --mark-grey: #c8c8c8;
  }
  * { margin: 0; padding: 0; box-sizing: border-box; }
  html, body { width: 848px; height: 1200px; overflow: hidden; background: var(--paper); }
  .letterhead {
    position: relative; width: 848px; height: 1200px; overflow: hidden;
    font-family: "Arimo", Arial, sans-serif; color: var(--ink); background: var(--paper);
  }
  .brand {
    position: absolute; left: 46px; top: 48px;
    display: flex; align-items: center; gap: 10px;
    font-size: 27px; font-weight: 700; color: var(--ink);
  }
  .brand-square { width: 14px; height: 14px; background: var(--brand-red); }
  .sender-block {
    position: absolute; left: 630px; top: 134px;
    font-size: 11.5px; line-height: 14px; font-weight: 700; font-style: normal;
  }
  .sender-block .company { color: var(--brand-red); }
  .sender-block p + p { margin-top: 10px; }
  .address-window { position: absolute; left: 53px; top: 272px; width: 285px; height: 152px; }
  .return-line {
    position: absolute; left: 85px; top: 290px;
    font-size: 7px; font-weight: 700; white-space: nowrap;
  }
  .return-line .company { color: var(--brand-red); }
  .letter-body p {
    position: absolute; left: 77px; width: 770px;
    font-size: 13.3px; line-height: 17.6px; white-space: nowrap;
  }
  .letter-body .subject { font-weight: 700; }
  .footer-rule { position: absolute; left: 0; top: 1098px; width: 848px; height: 6px; background: var(--brand-red); }
  .footer-band { position: absolute; left: 0; top: 1110px; width: 848px; height: 90px; background: var(--band-black); }
  .footer-info {
    position: absolute; left: 0; right: 0; top: 1155px;
    text-align: center; color: #fff; font-size: 11.5px; line-height: 18px; font-weight: 700;
  }
  .footer-info .accent { color: var(--brand-red); }
</style>
</head>
<body>
<main class="letterhead">
  <div class="brand"><span class="brand-square"></span><span>Velmora Systemhaus</span></div>

  <address class="sender-block">
    <p><span class="company">Velmora Systemhaus</span><br>Lindenweg 12<br>73465 Beispielstadt</p>
    <p>Tel: 07231 - 48210<br>Fax: 07231 - 48219</p>
    <p>info@velmora-systemhaus.de<br>www.velmora-systemhaus.de</p>
  </address>

  <svg class="address-window" viewBox="0 0 285 152" aria-hidden="true">
    <g fill="none" stroke="var(--mark-grey)" stroke-width="2">
      <path d="M1 12 V1 H12"/><path d="M273 1 H284 V12"/>
      <path d="M1 140 V151 H12"/><path d="M273 151 H284 V140"/>
    </g>
  </svg>
  <div class="return-line"><span class="company">Velmora Systemhaus</span> • Lindenweg 12 • 73465 Beispielstadt</div>

  <section class="letter-body">
    <p class="subject" style="top:496px">Betreff: Musterbrief Velmora Systemhaus</p>
    <p style="top:531px">Sehr geehrte Damen und Herren,</p>
    <p style="top:566px">Lorem ipsum dolor sit amet, consectetur adipiscing elit, set eiusmod tempor incidunt et labore et dolore magna aliquam.<br>Ut enim ad minim veniam, quis nostrud exerc. Irure dolor in reprehend incididunt ut labore et dolore magna aliqua. Ut as<br>enim ad minim veniam, quis nostrud exercitation ullamco laboris nisi ut aliquip ex ea commodo consequat. Duis aute iru<br>dolor in repreh.</p>
    <p style="top:669px">At vver eos et accusam dignissum qui blandit est praesent. Trenz pruca beynocguon doas nog apoply su trenz ucu hugh<br>rasoluguon monugor or trenz ucugwo jag scannar. Wa hava laasad trenzsa gwo producgs su IdfoBraid, yop quiel geg ba<br>solaly rasponsubla rof trenzur sala ent dusgrubuguon. Offoctivo immoriatoly, hawrgaxeeis phat eit sakem eit vory gast te<br>Plok peish ba useing phen roxas Eslo idaffacgad gef trenz beynocguon quiel ba trenz Spraadshaag ent trenz dreek wirc<br>&nbsp;processidt program.</p>
    <p style="top:775px">Plloaso mako nuto uf cakso dodtos anr koop a cupy uf cak vux noaw yerw phuno. Whag schengos, uf efed, quiel ba mad<br>a su otrenzr swipontgwook proudgs hus yag su ba dagarmidad. Plasa maku noga wipont trenzsa schengos ent kaap zux</p>
    <p style="top:828px">copy wipont trenz kipgnaar mixent phona. Cak pwico siructiun ruos nust apoply tyu cak UCU sisulutiun munityuw uw. Tre<br>nz pruca beynocguon doas nog apoply su trenz ucu hugh rasoluguon monugor<br>&nbsp;or trenz ucugwo jag scannar. Wa hava la<br>asad trenzsa gwo producgs su IdfoBraid,yop quiel geg ba solaly rasponsubla rof trenzur sala ent dusgrubuguonwe red d</p>
    <p style="top:951px">Mit freundlichen Grüßen,</p>
    <p style="top:1023px">Miriam Keller</p>
  </section>

  <div class="footer-rule"></div>
  <div class="footer-band"></div>
  <footer class="footer-info">
    <div><span class="accent">Velmora Systemhaus</span> • Lindenweg 12 • 73465 Beispielstadt • <span class="accent">Tel</span> 0123 987 654 • <span class="accent">Fax</span> 0123 987 655</div>
    <div><span class="accent">Mail</span> info@velmora-systemhaus.de • Internet <span class="accent">www.velmora-systemhaus.de</span> • Kontonr 1234987 • BLZ 210987 Beispielbank</div>
  </footer>
</main>
</body>
</html>
```